Card design for orthopaedic surgeons working as The Brindlewood Orthopaedic Centre

Business cards, letterhead

Colors

Designer to choose colors to be used in the design.

Requirements
Must have
• Late addition.
• Cards letterhead must have logos of
• Corvane Federated Institute of Surgeons
• Meridale Orthopaedic Society
Nice to have
• Back of card to have space for appointment time to be added by hand and some blank space for writing incidental other notes.

```html
<!DOCTYPE html>
<html lang="en">
<head>
<meta charset="utf-8">
<title>The Brindlewood Orthopaedic Centre – Cards</title>
<link href="https://fonts.googleapis.com/css2?family=Roboto:wght@400;500;700&display=swap" rel="stylesheet">
<style>
  :root {
    --sky: #5aaae0;
    --navy: #0f2a42;
    --deep: #03324b;
    --paper: #ffffff;
    --backdrop: #b9b9b9;
  }
  * { box-sizing: border-box; margin: 0; padding: 0; }
  html, body { width: 1172px; height: 1200px; overflow: hidden; }
  body {
    background: var(--backdrop);
    font-family: 'Roboto', Arial, sans-serif;
    color: var(--navy);
    position: relative;
  }
  .card {
    position: absolute;
    left: 214px;
    width: 744px;
    height: 425px;
    background: var(--paper);
    border-radius: 28px;
    overflow: hidden;
  }
  .card--appointment { top: 122px; }
  .card--contact { top: 645px; height: 430px; }

  .wordmark {
    position: absolute;
    left: 0; right: 0;
    text-align: center;
    font-weight: 400;
    color: var(--navy);
    white-space: nowrap;
    letter-spacing: -0.3px;
  }
  .card--appointment .wordmark { top: 84px; font-size: 29px; }
  .card--contact .wordmark { top: 130px; font-size: 37px; }

  .appointment-title {
    position: absolute;
    top: 140px; left: 0; right: 0;
    text-align: center;
    font-weight: 700;
    font-size: 27px;
    color: var(--sky);
    letter-spacing: -0.2px;
  }
  .form-line {
    position: absolute;
    left: 52px; right: 52px;
    display: flex;
    align-items: baseline;
    font-size: 22px;
    white-space: nowrap;
  }
  .form-line .fill {
    flex: 1;
    border-bottom: 3px dotted var(--navy);
    margin: 0 2px;
    height: 1px;
  }
  .form-line--patient { top: 207px; }
  .form-line--when { top: 279px; }
  .form-line--when .gap { width: 12px; }
  .form-line--when .label { margin-right: 6px; }

  .weekdays {
    position: absolute;
    top: 350px; left: 52px; right: 52px;
    display: flex;
    justify-content: space-between;
    font-size: 21px;
    color: var(--sky);
  }
  .weekday { display: flex; align-items: center; gap: 9px; }
  .weekday .box {
    width: 19px; height: 19px;
    border: 2px solid var(--navy);
  }

  .doctor {
    position: absolute;
    top: 245px; right: 392px;
    text-align: right;
  }
  .doctor-name {
    font-weight: 700;
    font-size: 32px;
    color: var(--sky);
    letter-spacing: -0.3px;
    line-height: 1.1;
  }
  .doctor-role { font-size: 21px; margin-top: 3px; }
  .divider {
    position: absolute;
    left: 376px; top: 240px;
    width: 3px; height: 80px;
    background: var(--navy);
  }
  .contact-list {
    position: absolute;
    left: 398px; top: 234px;
    list-style: none;
    font-size: 21px;
  }
  .contact-list li {
    display: flex; align-items: center;
    height: 30px;
  }
  .contact-list svg { width: 15px; height: 15px; margin-right: 8px; fill: var(--sky); }

  .footer-stripe {
    position: absolute;
    left: 0; right: 0; bottom: 36px;
    height: 6px;
    background: var(--sky);
  }
  .footer-band {
    position: absolute;
    left: 0; right: 0; bottom: 0;
    height: 30px;
    background: var(--deep);
  }
</style>
</head>
<body>
  <section class="card card--appointment">
    <div class="wordmark">The Brindlewood Orthopaedic Centre</div>
    <h1 class="appointment-title">YOUR NEXT APPOINTMENT</h1>
    <div class="form-line form-line--patient">
      <span class="fill"></span><span>has an appointment</span>
    </div>
    <div class="form-line form-line--when">
      <span class="label">Date:</span><span class="fill"></span>
      <span class="gap"></span>
      <span class="label">Time:</span><span class="fill"></span><span>AM/PM</span>
    </div>
    <div class="weekdays">
      <span class="weekday">Sun <span class="box"></span></span>
      <span class="weekday">Mon <span class="box"></span></span>
      <span class="weekday">Tue <span class="box"></span></span>
      <span class="weekday">Wed <span class="box"></span></span>
      <span class="weekday">Thu <span class="box"></span></span>
      <span class="weekday">Fri <span class="box"></span></span>
      <span class="weekday">Sat <span class="box"></span></span>
    </div>
  </section>

  <section class="card card--contact">
    <div class="wordmark">The Brindlewood Orthopaedic Centre</div>
    <div class="doctor">
      <div class="doctor-name">Dr. Elias Marlowe</div>
      <div class="doctor-role">Orthopaedic Specialist</div>
    </div>
    <div class="divider"></div>
    <ul class="contact-list">
      <li><svg viewBox="0 0 16 16" aria-hidden="true"><path d="M3.5 1.5l2.5 3-1.6 1.6c.9 1.9 2.4 3.4 4.3 4.3L10.3 8.8l3 2.5-1.4 2.9C6.6 14.2 1.8 9.4 1.5 3.6z"/></svg>614-802-3377</li>
      <li><svg viewBox="0 0 16 16" aria-hidden="true"><path d="M1 3.5h14v9H1z M2 4.5l6 4.5 6-4.5" stroke="#fff" stroke-width="1"/></svg>info@brindlewoodortho.com</li>
      <li><svg viewBox="0 0 16 16" aria-hidden="true"><circle cx="8" cy="8" r="7"/><path d="M4 5c2 0 2 2 4 2s1 3 3 3M9 2c0 2 2 2 3 3" stroke="#fff" stroke-width="1.2" fill="none"/></svg>www.brindlewoodortho.com</li>
    </ul>
    <div class="footer-stripe"></div>
    <div class="footer-band"></div>
  </section>
</body>
</html>
```